Nexor Turbo Business Card Design

This is a start up company that has state of the art patented technology for turbo chargers,that can be used on engines, gas or diesel, for any type of automotive,aviation,marine or industrial purpose.
This technology will provide longer life,lower maintenance and better performance and help produce lower emissions with any turbocharged engine.Red would be a predominate color and the design should communicate the latest technology,economy and
Environmental concern.
This product will initially be distributed in the U.S.A. But should move rapidly to global use.
Updates

Thank you for your design submissions, I have increased the budget for this job because my initial order was too low for the quality of work shown, plus I would Like to see some more options. I have a meeting this Sunday with my other partners and would anticipate being able to give you some feedback by the Beginning of next week. Regards.

Thank you for everyone's participation. The deadline is still open until 6/15 and my partners and I have a meeting Scheduled this weekend. At this time we have not ruled anyone out, But will be making a decision during the course of our meeting and wil Decide which direction we will be going in by the beginning of the week. Thanks again, regards, Dan Ferris.

Hello everybody, Sorry for the delay in communication, we have been very busy in putting the start up together. We are still not decided on the design of the business card and have a wide range to choose from. I would anticipated we shall have an answer within the next two weeks. Regards, Dan Ferris.

Target Market(s)

Manufacturers and wholesalers' of OEM and replacement turbochargers

Industry/Entity Type

Industrial

Contact Information for Business Card

We need a logo that should incorporate the " Nexor, a " possibly super imposed over a turbo charger with the fan blades of the turbocharger showing in the center of the "a" .
Name,title,phone number and email address only, no street/mailing address at this time.
The full name of the company is
" Nexor Turbo Technologies LLC "
For the initial card you can use my info.
Daniel Ferris
VP Sales & Marketing
dferris@nexorturbotechnologies.com
555 014 2876

Requirements
Must have
• The Nexor A, the outline of a turbo charger
Nice to have
• Something classy and simple and worldly (global)
Should not have
• No engines,cars,boats,planes

```html
<!DOCTYPE html>
<html lang="en">
<head>
<meta charset="UTF-8">
<title>Nexor Turbo Technologies LLC – Business Card</title>
<link rel="stylesheet" href="https://fonts.googleapis.com/css2?family=Federo&display=swap">
<style>
  :root {
    --card-black: #060606;
    --turbo-red: #ff0000;
    --turbo-red-deep: #b80000;
    --text-white: #ffffff;
    --mark-black: #050505;
  }
  html, body {
    margin: 0;
    padding: 0;
    width: 1200px;
    height: 664px;
    overflow: hidden;
    background: var(--card-black);
  }
  .card {
    position: relative;
    width: 1200px;
    height: 664px;
    overflow: hidden;
    background: var(--card-black);
    font-family: "Federo", sans-serif;
    color: var(--text-white);
  }
  .turbo-artwork {
    position: absolute;
    left: 430px;
    top: 0;
    width: 770px;
    height: 664px;
    background:
      radial-gradient(circle at 505px 345px,
        var(--turbo-red) 0 120px,
        var(--mark-black) 121px 150px,
        var(--turbo-red) 151px 200px,
        var(--turbo-red-deep) 230px,
        var(--turbo-red) 300px,
        rgba(255,0,0,0.55) 360px,
        rgba(6,6,6,0) 470px);
  }
  .turbo-mark {
    position: absolute;
    left: 935px;
    top: 345px;
    transform: translate(-50%, -50%);
    font-size: 48px;
    color: var(--mark-black);
    letter-spacing: 1px;
  }
  .company-name {
    position: absolute;
    left: 22px;
    top: 4px;
    margin: 0;
    font-size: 70px;
    font-weight: 400;
    letter-spacing: 2px;
    white-space: nowrap;
    line-height: 1.2;
  }
  .person {
    position: absolute;
    left: 60px;
    top: 326px;
    width: 690px;
    text-align: center;
    font-size: 52px;
    line-height: 66px;
    letter-spacing: 1px;
  }
  .person-name, .person-title { display: block; }
  .contact-phone {
    position: absolute;
    left: 255px;
    top: 532px;
    font-size: 38px;
    letter-spacing: 1px;
  }
  .contact-email {
    position: absolute;
    left: 38px;
    top: 592px;
    font-size: 38px;
    letter-spacing: 0.5px;
  }
</style>
</head>
<body>
  <div class="card">
    <div class="turbo-artwork" role="img" aria-label="Red stencil-style illustration of a turbocharger housing"></div>
    <div class="turbo-mark">Nexor</div>

    <h1 class="company-name">Nexor Turbo Technologies LLC</h1>

    <div class="person">
      <span class="person-name">Daniel Ferris</span>
      <span class="person-title">VP Sales &amp; Marketing</span>
    </div>

    <div class="contact-phone">555 014 2876</div>
    <div class="contact-email">dferris@nexorturbotechnologies.com</div>
  </div>
</body>
</html>
```